Letterhead design of KESTREL POWER THRIFT INC.

we are a energy saving company doing the solar screen, radian barrier, attic insulation, double panel windows. Basically i need the design of the letterhead including my company name, business address, phone numbers, fax number and email address. Main thing i need it look like a huge company and look like very high class. thanks !!

Reason: Please send me more new design about my company! Thanks so much!!

Industry/Entity Type

Business

```html
<!DOCTYPE html>
<html lang="en">
<head>
<meta charset="utf-8">
<title>Kestrel Power Thrift Inc. — Letterhead</title>
<link rel="stylesheet" href="https://fonts.googleapis.com/css2?family=Arimo:wght@400;700&display=swap">
<style>
  :root {
    --ink: #111111;
    --leaf-green: #8fc31f;
    --frame: #9a9a9a;
    --paper: #ffffff;
    --ghost: #eeeeee;
  }
  html, body {
    margin: 0;
    padding: 0;
    width: 928px;
    height: 1200px;
    overflow: hidden;
    background: var(--paper);
  }
  .letterhead {
    position: relative;
    width: 928px;
    height: 1200px;
    box-sizing: border-box;
    border: 1px solid var(--frame);
    background: var(--paper);
    font-family: "Arimo", Arial, sans-serif;
    overflow: hidden;
  }
  .backdrop {
    position: absolute;
    left: 0;
    top: 0;
  }
  .ghost-mark {
    font-family: "Arimo", Arial, sans-serif;
    font-weight: 700;
    font-size: 150px;
    fill: var(--ghost);
  }
  .ghost-name {
    font-family: "Arimo", Arial, sans-serif;
    font-weight: 400;
    font-size: 68px;
    fill: var(--ghost);
  }
  .brand {
    position: absolute;
    left: 80px;
    top: 112px;
    display: flex;
    align-items: center;
    gap: 10px;
  }
  .brand-square {
    width: 20px;
    height: 20px;
    background: var(--leaf-green);
  }
  .brand-name {
    font-weight: 700;
    font-size: 22px;
    color: var(--ink);
  }
  .header-rule {
    position: absolute;
    left: 0;
    top: 166px;
    width: 100%;
    height: 12px;
    background: var(--leaf-green);
  }
  .contact {
    position: absolute;
    left: 687px;
    top: 190px;
    margin: 0;
    font-style: normal;
    font-weight: 700;
    font-size: 13.5px;
    line-height: 16.5px;
    color: var(--ink);
  }
  .contact span { display: block; }
</style>
</head>
<body>
  <div class="letterhead">
    <svg class="backdrop" width="928" height="1200" viewBox="0 0 928 1200" aria-hidden="true">
      <text class="ghost-mark" x="464" y="610" text-anchor="middle">KESTREL</text>
      <text class="ghost-mark" x="464" y="785" text-anchor="middle">POWER</text>
      <text class="ghost-mark" x="464" y="960" text-anchor="middle">THRIFT</text>
      <text class="ghost-name" x="464" y="1086" text-anchor="middle">Kestrel Power Thrift Inc.</text>
    </svg>

    <div class="brand">
      <div class="brand-square"></div>
      <div class="brand-name">Kestrel Power Thrift Inc.</div>
    </div>

    <div class="header-rule"></div>

    <address class="contact">
      <span>2870 Larkfield Rd Suite #300</span>
      <span>Dallas,Texas 75201</span>
      <span>ph: 555-014-2290</span>
      <span>Fax: 555-014-7731</span>
      <span>kestrelpowerthrift@example.com</span>
    </address>
  </div>
</body>
</html>
```